Maritime Law Firm Business Card Design Project

We are a new maritime law firm starting in Queensland, Australia. The principal is a master mariner as well as a lawyer and is looking for a logo design that evokes a practical and user-friendly approach to the law, as well as maritime law expertise.

We would like to use the compass rose as the foundation for the design, as it symbolises clarity of direction and purpose, as well as traditional maritime heritage.

The 16th Century Luis Bercedo Compass Rose (attached) is beautiful, but is too complex for a logo. A simplified version is desired.

Colour Paletter s flexible, although a B&W version is also needed. Colour suggestions are navy blue (for the sea), red and green (navigation lights) and maroon (for Queensland).

Target Market(s)

Maritime Industry/legal services

Industry/Entity Type

Law Firm

Font styles to use
Sans Serif

Requirements
Must have
• Contact Details
Name of 'Pellworth Legal'

```html
<!DOCTYPE html>
<html lang="en">
<head>
<meta charset="utf-8">
<title>Pellworth Legal — Business Card</title>
<link rel="stylesheet" href="https://fonts.googleapis.com/css2?family=Arimo:wght@400&display=swap">
<style>
  :root {
    --navy: #1c2438;
    --edge: #9aa0a8;
    --signal-red: #c9293f;
    --starboard-green: #13873a;
    --maroon: #7b2c48;
  }
  * { margin: 0; padding: 0; box-sizing: border-box; }
  html, body {
    width: 1200px;
    height: 776px;
    overflow: hidden;
    background: var(--navy);
  }
  .card {
    position: relative;
    width: 1200px;
    height: 776px;
    background: var(--navy);
    border: 1px solid var(--edge);
    font-family: "Arimo", Arial, sans-serif;
    font-weight: 400;
  }
  .card p { position: absolute; white-space: nowrap; line-height: 1; }
  .brand-mark {
    position: absolute;
    left: 22px;
    top: 40px;
    display: flex;
    align-items: center;
    gap: 16px;
  }
  .brand-mark__dot {
    width: 120px;
    height: 120px;
    border-radius: 50%;
    background: var(--signal-red);
  }
  .brand-mark__name {
    color: var(--signal-red);
    font-size: 30px;
  }
  .firm-name {
    right: 36px;
    top: 20px;
    color: var(--signal-red);
    font-size: 45px;
  }
  .person-name {
    left: 437px;
    top: 286px;
    color: var(--starboard-green);
    font-size: 45px;
  }
  .contact-phone {
    left: 437px;
    top: 414px;
    color: var(--maroon);
    font-size: 45px;
  }
  .contact-email {
    left: 437px;
    top: 471px;
    color: var(--maroon);
    font-size: 45px;
  }
  .practice-area {
    left: 14px;
    top: 720px;
    color: var(--signal-red);
    font-size: 45px;
  }
</style>
</head>
<body>
  <main class="card">
    <div class="brand-mark">
      <span class="brand-mark__dot" aria-hidden="true"></span>
      <span class="brand-mark__name">Pellworth Legal</span>
    </div>
    <p class="firm-name">Pellworth Legal</p>
    <p class="person-name">Martin Hale</p>
    <p class="contact-phone">0400-381-752</p>
    <p class="contact-email">m.hale.law@mailbox.com</p>
    <p class="practice-area">Maritime Law</p>
  </main>
</body>
</html>
```